Dental Specialist Needs a Business Card

We are a state of the art dental specialty office and need a business card that looks modern but professional.
I have provided our logo design in both vertical and horizontal. We use the design on letterhead in the vertical format but provided both forms for you. Thanks
Updates

Please add the address, phone and fax numbers I listed to all designs and please leave a space for website and for my employee name on each design. Thanks 2847 Marlow Avenue, Suite K East Brantham, NY 14391 Phone (716)392-5174 Fax:(716)392-5179 My name is Devin R.Holloway,D.D.S. If you want to show it with my name but the design needs to allow for the name to be switched.

Industry/Entity Type

Business

```html
<!DOCTYPE html>
<html lang="en">
<head>
<meta charset="utf-8">
<title>Keystone Endodontics P.C. – Business Card</title>
<link rel="stylesheet" href="https://fonts.googleapis.com/css2?family=Noto+Sans:wght@400&display=swap">
<style>
  :root {
    --card-bg: #0a0a0a;
    --brand-white: #ffffff;
    --brand-blue: #5ec2f0;
    --brand-green: #8fe32c;
    --divider: #e6e6e6;
  }
  html, body {
    margin: 0;
    padding: 0;
    width: 1200px;
    height: 741px;
    overflow: hidden;
    background: var(--card-bg);
  }
  .card {
    position: relative;
    width: 1200px;
    height: 741px;
    background: var(--card-bg);
    font-family: "Noto Sans", Verdana, sans-serif;
    overflow: hidden;
  }
  .brand-mark {
    position: absolute;
    left: 250px;
    top: 100px;
  }
  .brand-divider {
    position: absolute;
    left: 479px;
    top: 81px;
    width: 2px;
    height: 245px;
    background: var(--divider);
  }
  .brand-name {
    position: absolute;
    left: 506px;
    top: 140px;
    margin: 0;
    color: var(--brand-white);
    font-weight: 400;
    line-height: 1;
  }
  .brand-name .primary {
    display: block;
    font-size: 96px;
    letter-spacing: 0.01em;
  }
  .brand-name .secondary {
    display: block;
    margin-top: 22px;
    margin-left: 72px;
    font-size: 36px;
    letter-spacing: 0.22em;
  }
  .practitioner {
    position: absolute;
    left: 224px;
    top: 364px;
    margin: 0;
    color: var(--brand-blue);
    font-weight: 400;
    font-size: 55px;
    letter-spacing: 0.01em;
    line-height: 1;
  }
  .contact {
    position: absolute;
    left: 225px;
    top: 450px;
    margin: 0;
    color: var(--brand-green);
    font-style: normal;
    font-size: 31px;
    line-height: 46px;
    letter-spacing: 0.02em;
  }
</style>
</head>
<body>
  <main class="card">
    <svg class="brand-mark" width="170" height="170" viewBox="0 0 170 170" aria-hidden="true">
      <circle cx="85" cy="85" r="80" fill="var(--brand-blue)"/>
    </svg>
    <div class="brand-divider"></div>
    <h1 class="brand-name">
      <span class="primary">KEYSTONE</span>
      <span class="secondary">Endodontics P.C.</span>
    </h1>
    <h2 class="practitioner">Devin R. Holloway D.D.S.</h2>
    <address class="contact">
      2847 Marlow Avenue, Suite K<br>
      East Brantham, NY 14391<br>
      Ph:(716)392-5174<br>
      Fax: (716)392-5179
    </address>
  </main>
</body>
</html>
```